Design eines Praxisschilds für Hausarztpraxis
Zielgruppe
Hausarztpraxis, Zielgruppe sind die Bewohner vor Ort, bodenständig
Aufgabenstellung
Praxisschild entwerfen, es soll schlicht sein. Das angefügte Logo bitte verwenden, ggf. auch nur das Symbol ohne Namen verwenden und den Namen extra in schwarz aufführen.
Farben:
- schwarz
- Pantone 13-0645 Limeade
- Pantone 7726
Text:
Dr. med. Jonas Walbrecht
Facharzt für Innere Medizin
Facharzt für Allgemeinmedizin
Sprechzeiten:
Montag bis Freitag 07:30 – 12:00 Uhr
Dienstag und Donnerstag 17:00 – 19:00 Uhr
und nach Vereinbarung
Tel: 0761 83172
www.hausarzt-beispielau.de
Format quer (die Maße sind leider vorgegeben): 55,7 cm x 42,8 cm

```html
<!DOCTYPE html>
<html lang="de">
<head>
<meta charset="utf-8">
<title>Praxisschild – Dr. med. Jonas Walbrecht</title>
<link rel="stylesheet" href="https://fonts.googleapis.com/css2?family=Poppins:wght@400;600&family=Arimo:wght@400&display=swap">
<style>
  :root {
    --limeade: #cdda52;
    --pantone-7726: #00784a;
    --ink: #111111;
    --paper: #ffffff;
    --frame: #222222;
  }
  * { margin: 0; padding: 0; box-sizing: border-box; }
  html, body {
    width: 1200px;
    height: 1200px;
    overflow: hidden;
    background: var(--paper);
  }
  .canvas {
    position: relative;
    width: 1200px;
    height: 1200px;
  }
  .sign {
    position: absolute;
    left: 67px;
    top: 186px;
    width: 1080px;
    height: 829px;
    border: 1.2px solid var(--frame);
    background: var(--paper);
  }
  .brand-mark {
    position: absolute;
    left: 439px;
    top: 95px;
    width: 200px;
    height: 200px;
    border-radius: 50%;
    background: var(--limeade);
  }
  .practice-name {
    position: absolute;
    left: 0;
    width: 100%;
    top: 325px;
    text-align: center;
    font-family: "Poppins", sans-serif;
    font-weight: 600;
    font-size: 80px;
    line-height: 1;
    letter-spacing: -0.5px;
    color: var(--limeade);
  }
  .tagline {
    position: absolute;
    left: 0;
    width: 100%;
    top: 437px;
    text-align: center;
    font-family: "Poppins", sans-serif;
    font-weight: 400;
    font-size: 30px;
    line-height: 1;
    letter-spacing: 6px;
    text-transform: uppercase;
    color: var(--pantone-7726);
  }
  .info {
    position: absolute;
    top: 562px;
    font-family: "Arimo", Arial, sans-serif;
    font-size: 23.5px;
    line-height: 36px;
    color: var(--ink);
    list-style: none;
  }
  .info--doctor { left: 116px; }
  .info--hours { left: 646px; }
</style>
</head>
<body>
<div class="canvas">
  <section class="sign">
    <div class="brand-mark" aria-hidden="true"></div>
    <h1 class="practice-name">Dr. Jonas Walbrecht</h1>
    <p class="tagline">Ihr Hausarzt in Beispielau</p>

    <ul class="info info--doctor">
      <li>Dr. med. Jonas Walbrecht</li>
      <li>Facharzt für Innere Medizin</li>
      <li>Facharzt für Allgemeinmedizin</li>
      <li>www.hausarzt-beispielau.de</li>
    </ul>

    <ul class="info info--hours">
      <li>Sprechzeiten:</li>
      <li>Mo – Fr: 07:30 – 12:00 Uhr</li>
      <li>Di – Do: 17:00 – 19:00 Uhr</li>
      <li>und nach Vereinbarung</li>
      <li>Telefon: 0761 83172</li>
    </ul>
  </section>
</div>
</body>
</html>
```